Hvac and insulation company needs good looking business card design

We are hvac and insulation company and looking for a new business cards that look to today standards designs

Target Market(s)

homeowners

Industry/Entity Type

Hvac

Contact Information for Business Card

Name: Dorian Velkova
Home comfort consultant
address: 4827 Marrow Ridge Rd #215 Oakland, CA 94611
office: 888-317-5069
cell: 510-642-1388
Lic.# 458127
Email: dorian@quarry-hvac.com
Web: quarry-hvac.com

Requirements
Must have
• clean and sleek look
Nice to have
• simple with a clean look
Should not have
• to busy business card

```html
<!DOCTYPE html>
<html lang="en">
<head>
<meta charset="utf-8">
<title>Quarry Home Solutions – Business Card</title>
<link rel="stylesheet" href="https://fonts.googleapis.com/css2?family=Roboto:wght@400;500;700&display=swap">
<style>
  :root {
    --stage: #101010;
    --card-dark: #333335;
    --card-dark-edge: #2a2a2c;
    --orange: #f5892a;
    --orange-light: #f7a04f;
    --white: #ffffff;
    --ink-grey: #5f5f5f;
    --soft-grey: #9a9a9a;
  }
  * { box-sizing: border-box; margin: 0; padding: 0; }
  html, body { width: 1200px; height: 1000px; overflow: hidden; }
  body {
    background: var(--stage);
    font-family: "Roboto", Arial, sans-serif;
    position: relative;
  }
  .card {
    position: absolute;
    top: 355px;
    width: 500px;
    height: 290px;
    border-radius: 22px;
    overflow: hidden;
  }
  /* Back of card */
  .card-back {
    left: 70px;
    background: linear-gradient(135deg, var(--card-dark) 0%, var(--card-dark-edge) 100%);
  }
  .brand {
    position: absolute;
    left: 130px;
    top: 88px;
    display: flex;
    align-items: center;
    gap: 14px;
  }
  .brand-mark {
    width: 26px;
    height: 26px;
    border-radius: 50%;
    background: var(--orange);
  }
  .brand-name {
    color: var(--orange);
    font-weight: 700;
    font-size: 54px;
    letter-spacing: 0.5px;
    line-height: 1;
  }
  .brand-tagline {
    position: absolute;
    left: 170px;
    top: 150px;
    color: var(--soft-grey);
    font-size: 15px;
    letter-spacing: 2px;
  }
  .website {
    position: absolute;
    left: 0;
    right: 0;
    bottom: 44px;
    text-align: center;
    color: var(--orange);
    font-size: 16px;
    letter-spacing: 1.5px;
  }
  /* Front of card */
  .card-front {
    left: 630px;
    background: var(--white);
  }
  .wave { position: absolute; inset: 0; }
  .person {
    position: absolute;
    left: 34px;
    top: 26px;
  }
  .person-name {
    color: var(--orange);
    font-weight: 700;
    font-size: 24px;
  }
  .person-title {
    color: var(--ink-grey);
    font-size: 16px;
    font-weight: 500;
    margin-top: 2px;
  }
  .contact-list {
    position: absolute;
    left: 34px;
    top: 98px;
    list-style: none;
  }
  .contact-list li {
    display: flex;
    align-items: center;
    gap: 9px;
    color: var(--ink-grey);
    font-size: 14px;
    line-height: 19px;
  }
  .contact-list svg { width: 12px; height: 12px; flex: none; }
  .address {
    position: absolute;
    left: 34px;
    top: 220px;
    color: var(--white);
    font-weight: 500;
    font-size: 14px;
    line-height: 18px;
  }
  .front-brand {
    position: absolute;
    right: 34px;
    bottom: 34px;
    color: var(--white);
    font-weight: 700;
    font-size: 52px;
    line-height: 1;
  }
</style>
</head>
<body>

  <section class="card card-back" aria-label="Card back">
    <div class="brand">
      <span class="brand-mark"></span>
      <span class="brand-name">quarry</span>
    </div>
    <p class="brand-tagline">home solutions</p>
    <p class="website">www.quarry-hvac.com</p>
  </section>

  <section class="card card-front" aria-label="Card front">
    <svg class="wave" viewBox="0 0 500 290" preserveAspectRatio="none" aria-hidden="true">
      <defs>
        <linearGradient id="orangeBand" x1="0" y1="0" x2="1" y2="0">
          <stop offset="0" stop-color="#f7a04f"/>
          <stop offset="1" stop-color="#f5892a"/>
        </linearGradient>
      </defs>
      <path d="M0,165 C80,170 130,206 230,206 C340,206 380,152 500,150 L500,290 L0,290 Z" fill="url(#orangeBand)"/>
    </svg>

    <div class="person">
      <h1 class="person-name">Dorian Velkova</h1>
      <p class="person-title">Director</p>
    </div>

    <ul class="contact-list">
      <li>
        <svg viewBox="0 0 12 12"><path d="M2.5 1 L4.5 1 L5 3.5 L3.8 4.4 C4.4 5.8 5.6 7.2 7.3 8 L8.3 6.8 L11 7.3 L11 9.5 C11 10.3 10.3 11 9.5 11 C5 10.8 1.2 7 1 2.5 C1 1.7 1.7 1 2.5 1 Z" fill="#f5892a"/></svg>
        888-317-5069
      </li>
      <li>
        <svg viewBox="0 0 12 12"><rect x="3" y="0.8" width="6.5" height="10.4" rx="1" fill="none" stroke="#f5892a" stroke-width="1.2"/></svg>
        510-642-1388
      </li>
      <li>
        <svg viewBox="0 0 12 12"><rect x="0.8" y="2.5" width="10.4" height="7.5" fill="#f5892a"/><path d="M0.8 2.5 L6 6.5 L11.2 2.5" fill="none" stroke="#ffffff" stroke-width="1"/></svg>
        dorian@quarry-hvac.com
      </li>
    </ul>

    <p class="address">4827 Marrow Ridge Rd #215<br>Oakland, CA 94611</p>

    <p class="front-brand">quarry</p>
  </section>

</body>
</html>
```